Modern and appealing business Wordpress site

I've been operating my consulting firm for 5 years and feel like it is time to really improve on my web presence as I'm starting to get more national attention. I had a logo made through this service a couple of years ago, and would like to get a website that matches the look of it. The website will be used to (1) advertise my services (2) provide a brief overview of our management philosophies, and (3) host a resource library database. I understand HTML, but am not as familiar with how to code Wordpress, so I need someone that can help upload themes.

The website can be found at www.trelmondgroup.com.

For design, I prefer round designs to square and want the color scheme to match the attached logo. I have included both the full logo and the abbreviated one.

I also have a new picture for CFO uploaded. I plan on getting a new one for the CEO in the coming weeks, so I would like someone that I could get to help make the modification at a later time.

The resource database will be put into a document library (probably Kiln7) once the final design is completed rather than having multiple pages with links...just so you know the final vision for the site.

Reach out if you have any questions.

Target Market(s)

Community Action Agencies, Nonprofit Organization Leaders

Industry/Entity Type

Consulting

Coding

Coded - Design and coding required

Font styles to use
Sans Serif

Requirements
Must have
• Must match the color scheme of the attached logo

```html
<!DOCTYPE html>
<html lang="en">
<head>
<meta charset="utf-8">
<title>Trelmond Group — Leading Organizations to Excellence</title>
<link rel="stylesheet" href="https://fonts.googleapis.com/css2?family=Arimo:wght@400;700&display=swap">
<style>
:root{
  --blue:#2ea3dc;
  --blue-dark:#1f86bb;
  --charcoal:#474a4f;
  --ink:#2b2d30;
  --text:#6b6f75;
  --light:#f3f5f7;
  --line:#dfe3e7;
  --footer:#1d1f22;
  --canvas:#e9ecef;
  --white:#ffffff;
}
*{box-sizing:border-box;margin:0;padding:0}
html,body{width:1200px;height:3456px;overflow:hidden;background:var(--canvas);font-family:"Arimo",Arial,sans-serif;color:var(--text)}
.page{position:absolute;left:200px;top:0;width:800px;height:3456px;background:var(--white);overflow:hidden}
.abs{position:absolute}
.topbar{left:0;top:0;width:800px;height:20px;background:var(--blue);display:flex;align-items:center;padding-left:90px;gap:8px}
.topbar i{width:6px;height:6px;border-radius:50%;background:var(--white);display:block}
.header{left:0;top:20px;width:800px;height:60px;background:rgba(255,255,255,.94);display:flex;align-items:center;justify-content:space-between;padding:0 80px;z-index:3}
.brand{display:flex;align-items:center;gap:8px;font-weight:700;font-size:17px;color:var(--blue);letter-spacing:.5px}
.brand .dot{width:22px;height:22px;border-radius:50%;background:var(--blue)}
.nav{display:flex;gap:20px;font-size:10px;color:var(--ink);text-transform:uppercase}
.hero{left:0;top:20px;width:800px;height:460px;background:linear-gradient(160deg,#cfd9e2 0%,#9fb0c0 40%,#6e8397 75%,#53687c 100%)}
.hero-copy{left:110px;top:250px;color:var(--white)}
.hero-copy .lead{font-size:26px}
.hero-copy .big{font-size:32px;font-weight:700;letter-spacing:.5px}
.btn{display:inline-block;font-size:10px;padding:8px 16px;border-radius:14px;color:var(--white);background:var(--blue)}
.btn.dark{background:var(--charcoal)}
.hero-wave{left:0;top:380px;width:800px;height:100px}
.badge{left:385px;top:482px;width:30px;height:30px;border-radius:50%;background:var(--blue);border:4px solid var(--white);box-shadow:0 0 0 1px var(--line)}
h2{font-weight:400;font-size:26px;color:var(--ink)}
h2 b{color:var(--blue);font-weight:700}
.story{left:110px;top:560px;width:330px}
.story p{font-size:10px;line-height:1.6;margin:14px 0}
.story-mark{left:480px;top:570px;width:210px;height:210px;border-radius:50%;background:radial-gradient(circle at 40% 40%,#e7edf2,#c9d3dc)}
.services{left:0;top:850px;width:800px;height:320px;display:flex}
.service{flex:1;padding:60px 30px 0;color:var(--white);background:var(--blue)}
.service.mid{background:var(--charcoal)}
.service h3{font-size:13px;text-align:center;margin-bottom:14px}
.service p{font-size:9.5px;line-height:1.65;text-align:center}
.service-curve{left:0;top:850px;width:800px;height:50px}
.section-title{left:0;width:800px;text-align:center}
.team{left:130px;top:1270px;width:540px;display:flex;justify-content:space-between}
.member{width:250px;display:flex;gap:14px;align-items:center;background:var(--light);border-radius:8px;padding:12px}
.member .photo{width:90px;height:100px;border-radius:6px;background:linear-gradient(180deg,#c7d1da,#8a98a6)}
.member h4{font-size:11px;color:var(--ink)}
.member span{font-size:9px;display:block;margin:4px 0 10px}
.mission-wheel{left:110px;top:1510px;width:280px;height:280px;border-radius:50%;background:radial-gradient(circle,#ffffff 0 22%,#5b6066 23% 45%,var(--blue) 46% 100%)}
.mission{left:430px;top:1560px;width:280px}
.mission .rule{width:30px;height:2px;background:var(--blue);margin-bottom:10px}
.mission p{font-size:10px;line-height:1.6;margin:12px 0}
.mission ul{list-style:none;font-size:10px;line-height:1.9}
.mission li::before{content:"";display:inline-block;width:6px;height:6px;border-radius:50%;background:var(--blue);margin-right:8px}
.testi-bg{left:0;top:1860px;width:800px;height:380px;background:linear-gradient(120deg,#e6ecf1,#cdd8e1 50%,#e9eef2)}
.testi-curves{left:0;top:1860px;width:800px;height:380px}
.testi{left:150px;top:1930px;width:500px;text-align:center}
.testi .quote{font-size:48px;color:var(--ink);line-height:1;margin:10px 0 0;font-weight:700}
.testi p{font-size:10.5px;line-height:1.7;color:var(--ink)}
.testi .who{margin-top:14px;font-size:9px;color:var(--text)}
.resources{left:100px;top:2360px;width:600px;display:flex;justify-content:space-between}
.resource{width:180px}
.resource .img{height:115px;background:linear-gradient(150deg,#a8c7dc,#5f89a8)}
.resource .cap{font-size:9px;text-align:center;padding:7px;background:var(--light);color:var(--ink)}
.resource.active .cap{background:var(--blue);color:var(--white)}
.contact{left:150px;top:2680px;width:500px}
.row{display:flex;gap:20px}
.field{flex:1}
.field label{font-size:9px;color:var(--ink);display:block;margin-bottom:4px}
.field .box{height:24px;border:1px solid var(--line)}
.field .box.tall{height:90px}
.send{text-align:center;margin-top:18px}
.footer{left:0;top:2930px;width:800px;height:526px;background:var(--footer);color:#b7bcc2}
.foot-brand{left:80px;top:60px}
.foot-brand p{font-size:9px;margin-top:16px;width:200px;line-height:1.6}
.foot-col{top:60px;font-size:10px}
.foot-col h5{font-size:11px;color:var(--white);margin-bottom:14px;letter-spacing:1px}
.foot-col li{list-style:none;line-height:2}
.contact-line{display:flex;align-items:center;gap:10px;margin-bottom:12px}
.contact-line i{width:22px;height:22px;border-radius:50%;background:var(--blue);display:block}
.copy{left:80px;top:470px;font-size:9px}
</style>
</head>
<body>
<div class="page">
  <div class="abs hero" role="img" aria-label="Photo of a consultant presenting to a team around a meeting table"></div>
  <div class="abs topbar"><i></i><i></i><i></i></div>
  <header class="abs header">
    <div class="brand"><span class="dot"></span>TRELMOND GROUP</div>
    <nav class="nav"><span>Home</span><span>About</span><span>Services</span><span>Team</span><span>Resources</span><span>Contact</span></nav>
  </header>
  <div class="abs hero-copy">
    <div class="lead">Leading Organizations</div>
    <div class="big">TO EXCELLENCE!</div>
    <div style="margin-top:16px"><span class="btn dark">Learn More</span></div>
  </div>
  <svg class="abs hero-wave" viewBox="0 0 800 100" preserveAspectRatio="none">
    <path d="M0 30 Q400 120 800 30 L800 100 L0 100Z" fill="#ffffff"/>
    <path d="M0 30 Q400 120 800 30" fill="none" stroke="#2ea3dc" stroke-width="2"/>
  </svg>
  <div class="abs badge"></div>

  <section class="abs story">
    <h2>Our <b>Story</b></h2>
    <p>For five years we have partnered with community action agencies and nonprofit leaders to build stronger teams, clearer plans and lasting results across the country.</p>
    <p>Our approach blends practical training, sound data and honest strategy so every organization we serve can focus on its people and mission.</p>
    <span class="btn">Read More</span>
  </section>
  <div class="abs story-mark" role="img" aria-label="Large round brand emblem"></div>

  <section class="abs services">
    <div class="service"><h3>Training &amp; Consulting</h3><p>Hands-on workshops and coaching that give boards, directors and staff the tools to lead with confidence and meet every standard of performance.</p></div>
    <div class="service mid"><h3>Data Analytics</h3><p>We turn program numbers into clear insight, helping agencies measure outcomes, report to funders and make smarter decisions for the people they serve.</p></div>
    <div class="service"><h3>Strategizing</h3><p>Guided planning sessions that align vision, goals and resources into a focused strategic plan your whole organization can follow and own.</p></div>
  </section>
  <svg class="abs service-curve" viewBox="0 0 800 50" preserveAspectRatio="none">
    <path d="M0 0 L800 0 L800 10 Q400 60 0 10Z" fill="#ffffff"/>
  </svg>

  <h2 class="abs section-title" style="top:1200px">Our <b>Team</b></h2>
  <section class="abs team">
    <div class="member"><div class="photo" role="img" aria-label="Portrait of the chief executive"></div><div><h4>Dana Rourke</h4><span>Chief Executive Officer</span><span class="btn">View Bio</span></div></div>
    <div class="member"><div class="photo" role="img" aria-label="Portrait of the chief financial officer"></div><div><h4>Miriam Voss</h4><span>Chief Financial Officer</span><span class="btn">View Bio</span></div></div>
  </section>

  <div class="abs mission-wheel" role="img" aria-label="Circular puzzle diagram of the management philosophy"></div>
  <section class="abs mission">
    <div class="rule"></div>
    <h2>Our <b>Mission</b></h2>
    <p>We help mission-driven organizations grow capacity, strengthen leadership and deliver better outcomes for their communities.</p>
    <ul>
      <li>Lead with integrity</li>
      <li>Decide with data</li>
      <li>Invest in people</li>
      <li>Plan for growth</li>
      <li>Serve the community</li>
    </ul>
  </section>

  <div class="abs testi-bg" role="img" aria-label="Faded photo of colleagues talking in an office"></div>
  <svg class="abs testi-curves" viewBox="0 0 800 380" preserveAspectRatio="none">
    <path d="M0 0 L800 0 L800 20 Q400 90 0 20Z" fill="#ffffff" opacity=".9"/>
    <path d="M0 380 L800 380 L800 350 Q400 290 0 350Z" fill="#ffffff" opacity=".9"/>
    <path d="M0 40 Q400 120 800 40" fill="none" stroke="#ffffff" stroke-width="3" opacity=".8"/>
  </svg>
  <section class="abs testi">
    <h2>Client <b>Testimonials</b></h2>
    <div class="quote">&#8220;</div>
    <p>Working with this team transformed how our agency plans and reports. Their training was practical, their data work was clear, and our board now leads with real confidence and a shared sense of direction.</p>
    <div class="who">— Executive Director, Regional Agency</div>
  </section>

  <h2 class="abs section-title" style="top:2290px">TG <b>Resources</b></h2>
  <section class="abs resources">
    <div class="resource"><div class="img" role="img" aria-label="Photo of a planning meeting"></div><div class="cap">Strategic Planning Guide</div></div>
    <div class="resource active"><div class="img" role="img" aria-label="Photo of a handshake"></div><div class="cap">Board Training Toolkit</div></div>
    <div class="resource"><div class="img" role="img" aria-label="Photo of a team at laptops"></div><div class="cap">Outcome Reporting Tips</div></div>
  </section>

  <h2 class="abs section-title" style="top:2610px">Contact <b>Us</b></h2>
  <section class="abs contact">
    <div class="row"><div class="field"><label>Name</label><div class="box"></div></div><div class="field"><label>Email</label><div class="box"></div></div></div>
    <div class="field" style="margin-top:12px"><label>Message</label><div class="box tall"></div></div>
    <div class="send"><span class="btn">Send</span></div>
  </section>

  <footer class="abs footer">
    <div class="abs foot-brand"><div class="brand"><span class="dot"></span>TRELMOND GROUP</div><p>Consulting for community action agencies and nonprofit leaders nationwide.</p></div>
    <div class="abs foot-col" style="left:380px"><h5>LINKS</h5><ul><li>Home</li><li>About</li><li>Services</li><li>Team</li><li>Resources</li><li>Contact</li></ul></div>
    <div class="abs foot-col" style="left:560px"><h5>CONTACT</h5>
      <div class="contact-line"><i></i>(555) 014-2281</div>
      <div class="contact-line"><i></i>info@trelmondgroup.com</div>
      <div class="contact-line"><i></i>www.trelmondgroup.com</div>
    </div>
    <div class="abs copy">© Trelmond Group. All rights reserved.</div>
  </footer>
</div>
</body>
</html>
```